Harbor Relay Group Letterhead Design

The project name sums it up. Just need a professional letterhead design / template we can use in our marketing folders.

Here's the address / contact info for the letterhead: Harbor Relay Group 4815 Maple Crest Ave Suite 210 League City, Texas 77419 346-507-3846 www.harborrelaygroup.us support@harborrelaygroup.us

```html
<!DOCTYPE html>
<html lang="en">
<head>
<meta charset="utf-8">
<title>Harbor Relay Group Letterhead</title>
<link href="https://fonts.googleapis.com/css2?family=Arimo:wght@400;700&display=swap" rel="stylesheet">
<style>
  :root {
    --backdrop: #e4e4e4;
    --paper: #ffffff;
    --brand-blue: #1455a6;
    --ink: #2a2a2a;
    --grey-dark: #6d6e71;
    --grey-light: #d6d7d9;
    --signature-tone: #eeeeee;
  }
  * { margin: 0; padding: 0; box-sizing: border-box; }
  html, body {
    width: 1069px;
    height: 1200px;
    overflow: hidden;
    background: var(--backdrop);
    font-family: "Arimo", Arial, sans-serif;
  }
  .letterhead {
    position: absolute;
    left: 124px;
    top: 21px;
    width: 820px;
    height: 1158px;
    background: var(--paper);
    overflow: hidden;
    color: var(--ink);
  }
  .brand-name {
    position: absolute;
    top: 110px;
    left: 0;
    width: 100%;
    text-align: center;
    font-weight: 700;
    font-size: 36px;
    letter-spacing: 0.5px;
    color: var(--brand-blue);
  }
  .letter-body {
    position: absolute;
    left: 47px;
    top: 318px;
    width: 726px;
    font-size: 13.4px;
    line-height: 23.7px;
  }
  .recipient { margin-bottom: 15px; }
  .letter-body p.paragraph {
    text-align: justify;
  }
  .paragraph + .paragraph { margin-top: 36px; }
  .closing { margin-top: 14px; }
  .signature-area {
    margin-top: 16px;
    width: 146px;
    height: 60px;
    background: var(--signature-tone);
  }
  .footer-wave {
    position: absolute;
    left: 0;
    bottom: 0;
    width: 820px;
    height: 196px;
    display: block;
  }
  .contact {
    position: absolute;
    right: 47px;
    top: 1022px;
    text-align: right;
    color: #ffffff;
    font-size: 13.4px;
    line-height: 18.5px;
  }
  .contact .address { margin-bottom: 5px; }
  .contact-line {
    display: flex;
    justify-content: flex-end;
    align-items: center;
    gap: 5px;
    height: 20.5px;
  }
  .contact-line svg { width: 12px; height: 12px; fill: #ffffff; }
</style>
</head>
<body>
  <main class="letterhead">
    <header class="brand-name">Harbor Relay Group</header>

    <section class="letter-body">
      <div class="recipient">
        <p>Mr/s</p>
        <p>First Name and Last Name</p>
        <p>Company Name</p>
        <p>Address</p>
      </div>
      <p class="paragraph">Lorem Ipsum is simply dummy text of the printing and typesetting industry. Lorem Ipsum has been the industry's standard dummy text ever since the 1500s, when an unknown printer took a galley of type and scrambled it to make a type specimen book. It has survived not only five centuries, but also the leap into electronic typesetting, remaining essentially unchanged. It was popularised in the 1960s.</p>
      <p class="paragraph">he standard chunk of Lorem Ipsum used since the 1500s is reproduced below for those interested. Sections 1.10.32 and 1.10.33 from "de Finibus Bonorum et Malorum" by Cicero are also reproduced in their exact original form, accompanied by English versions from the 1914 translation by H. Rackham. Lorem ipsum dolor sit amet, consectetur adipiscing elit, sed do eiusmod tempor incididunt ut labore et dolore magna aliqua.</p>
      <p class="paragraph">It is a long established fact that a reader will be distracted by the readable content of a page when looking at its layout. The point of using Lorem Ipsum is that it has a more-or-less normal distribution of letters, as opposed to using 'Content here, content here', making it look like readable English. Many desktop publishing packages and web page editors now .</p>
      <p class="closing">Your Sincerely,</p>
      <div class="signature-area" role="img" aria-label="Handwritten signature"></div>
    </section>

    <svg class="footer-wave" viewBox="0 1300 1107 264" preserveAspectRatio="none" aria-hidden="true">
      <defs>
        <linearGradient id="swoosh-grey" x1="0" y1="0" x2="1" y2="0">
          <stop offset="0" stop-color="var(--grey-dark)"/>
          <stop offset="0.55" stop-color="#a7a9ac"/>
          <stop offset="1" stop-color="var(--grey-light)"/>
        </linearGradient>
      </defs>
      <path fill="url(#swoosh-grey)" d="M0 1375 C80 1450 180 1482 270 1478 C500 1468 750 1322 950 1318 C750 1334 520 1500 280 1514 C180 1519 80 1490 0 1425 Z"/>
      <path fill="var(--brand-blue)" d="M0 1427 C100 1500 200 1524 300 1518 C550 1496 750 1332 900 1328 C1000 1326 1060 1358 1107 1380 L1107 1564 L0 1564 Z"/>
    </svg>

    <address class="contact" style="font-style:normal">
      <div class="address">
        <p>4815 Maple Crest Ave Suite</p>
        <p>210 League City Texas 77419</p>
      </div>
      <p class="contact-line">346-507-3846
        <svg viewBox="0 0 24 24"><path d="M6.6 10.8a15.1 15.1 0 0 0 6.6 6.6l2.2-2.2a1 1 0 0 1 1-.25 11.4 11.4 0 0 0 3.6.57 1 1 0 0 1 1 1V20a1 1 0 0 1-1 1A17 17 0 0 1 3 4a1 1 0 0 1 1-1h3.5a1 1 0 0 1 1 1c0 1.25.2 2.45.57 3.57a1 1 0 0 1-.25 1z"/></svg>
      </p>
      <p class="contact-line">support@harborrelaygroup.us
        <svg viewBox="0 0 24 24"><path d="M2 5h20v14H2z M2 5l10 8 10-8" fill="#ffffff" stroke="var(--brand-blue)" stroke-width="1.6"/></svg>
      </p>
      <p class="contact-line">www.harborrelaygroup.us
        <svg viewBox="0 0 24 24"><circle cx="12" cy="12" r="10"/><path d="M2 12h20M12 2c3 3 3 17 0 20M12 2c-3 3-3 17 0 20" fill="none" stroke="var(--brand-blue)" stroke-width="1.5"/></svg>
      </p>
    </address>
  </main>
</body>
</html>
```